New Business Card

Would like a shiny card with Metallic logo raised on th front. Address 518 Whitlock Avenue, Toronto Ontario M4K2J8, phone 416 555 0182, email kvbe@lindenmail.ca and web www.kvbe.ca on the back in right and left lower corners balanced. Top of back should say Personalized Care for Pet's and their People centered. Leaving space on the back to write. Horizontal placement

Industry/Entity Type

Business

```html
<!DOCTYPE html>
<html lang="en">
<head>
<meta charset="utf-8">
<title>Kestrel Vale Animal Hospital – Business Card</title>
<link href="https://fonts.googleapis.com/css2?family=Open+Sans:wght@400;600;700&display=swap" rel="stylesheet">
<style>
  :root {
    --backdrop: #e8e5e1;
    --card-dark: #2b2b2b;
    --card-light: #ffffff;
    --ink: #1e1e1e;
    --ink-soft: #3c3c3c;
    --silver: #c9c9c9;
    --silver-deep: #a9a9a9;
    --mark-grey: #555555;
    --rule: #2a2a2a;
  }
  * { margin: 0; padding: 0; box-sizing: border-box; }
  html, body {
    width: 1200px; height: 1000px; overflow: hidden;
    background: var(--backdrop);
    font-family: "Open Sans", Arial, sans-serif;
  }
  .canvas { position: relative; width: 1200px; height: 1000px; }
  .card {
    position: absolute; left: 267px; width: 665px;
    border-radius: 26px;
    box-shadow: 0 6px 18px rgba(0,0,0,.22);
  }
  .card-front { top: 75px; height: 396px; background: var(--card-dark); }
  .card-back { top: 533px; height: 398px; background: var(--card-light); }

  .tagline {
    position: absolute; top: 28px; width: 100%; text-align: center;
    color: #f2f2f2; font-size: 18px; font-weight: 400;
  }
  .front-mark {
    position: absolute; left: 262px; top: 100px; width: 140px; height: 140px;
    border-radius: 50%;
    background: radial-gradient(circle at 35% 30%, #e6e6e6, var(--silver-deep));
  }
  .front-name {
    position: absolute; top: 246px; width: 100%; text-align: center;
    color: var(--silver); font-weight: 600; letter-spacing: 1px;
    text-transform: uppercase; line-height: 1.15;
  }
  .front-name .line-1 { display: block; font-size: 34px; }
  .front-name .line-2 { display: block; font-size: 17px; letter-spacing: 2px; }

  .contact { position: absolute; left: 30px; top: 84px; color: var(--ink-soft); }
  .contact .person { font-size: 17px; font-weight: 600; color: var(--ink); }
  .contact .role { font-size: 16px; margin-top: 1px; }
  .contact .address { font-size: 15px; line-height: 23px; margin-top: 15px; padding-left: 2px; }
  .contact .lines { list-style: none; margin-top: 10px; font-size: 15px; line-height: 23.5px; padding-left: 2px; }
  .contact .lines li { display: flex; align-items: center; gap: 7px; }
  .contact .lines svg { width: 14px; height: 14px; fill: var(--ink); }

  .back-mark {
    position: absolute; left: 426px; top: 97px; width: 100px; height: 100px;
    border-radius: 50%; background: var(--mark-grey);
  }
  .back-name {
    position: absolute; left: 318px; top: 208px; width: 316px; text-align: center;
    color: var(--ink); font-weight: 600; text-transform: uppercase; line-height: 1.15;
  }
  .back-name .line-1 { display: block; font-size: 26px; letter-spacing: .5px; }
  .back-name .line-2 { display: block; font-size: 13px; letter-spacing: 1.5px; }

  .write-line {
    position: absolute; left: 31px; width: 603px; height: 0;
    border-top: 1.5px solid var(--rule);
  }
  .write-line.first { top: 326px; }
  .write-line.second { top: 363px; }
</style>
</head>
<body>
<main class="canvas">
  <section class="card card-front">
    <p class="tagline">Personalized Care for Pet's and their People</p>
    <div class="front-mark"></div>
    <h1 class="front-name"><span class="line-1">Kestrel Vale</span><span class="line-2">Animal Hospital</span></h1>
  </section>

  <section class="card card-back">
    <div class="contact">
      <p class="person">DANIEL OSTRANDER</p>
      <p class="role">President</p>
      <p class="address">518 Whitlock Avenue,<br>Toronto Ontario M4K2J8</p>
      <ul class="lines">
        <li><svg viewBox="0 0 16 16"><path d="M3 2h3l1.5 3.5-2 1.3a8 8 0 0 0 3.7 3.7l1.3-2L14 10v3a1 1 0 0 1-1 1A11 11 0 0 1 2 3a1 1 0 0 1 1-1z"/></svg>+ 000 000 000</li>
        <li><svg viewBox="0 0 16 16"><path d="M1 3h14v10H1z M2 4l6 5 6-5" fill="var(--ink)"/><path d="M2 4.5l6 4.6 6-4.6" stroke="#fff" stroke-width="1.2" fill="none"/></svg>kvbe@lindenmail.ca</li>
        <li><svg viewBox="0 0 16 16"><circle cx="8" cy="8" r="6.5" fill="none" stroke="var(--ink)" stroke-width="1.6"/><path d="M1.5 8h13M8 1.5c-3 3.5-3 9.5 0 13M8 1.5c3 3.5 3 9.5 0 13" fill="none" stroke="var(--ink)" stroke-width="1.2"/></svg>www.kvbe.ca</li>
      </ul>
    </div>
    <div class="back-mark"></div>
    <h2 class="back-name"><span class="line-1">Kestrel Vale</span><span class="line-2">Animal Hospital</span></h2>
    <div class="write-line first"></div>
    <div class="write-line second"></div>
  </section>
</main>
</body>
</html>
```